Real eatate

My company name is “Maple Crest Realestate” i would like to create a business card. I would like something modern and sleek similar to picture uploaded. All text in the business card should be black and the logo gold any shade.

```html
<!DOCTYPE html>
<html lang="en">
<head>
<meta charset="utf-8">
<title>Maple Crest Realestate — Business Card</title>
<link href="https://fonts.googleapis.com/css2?family=Montserrat:wght@500;700&family=Oswald:wght@500&display=swap" rel="stylesheet">
<style>
  :root {
    --backdrop: #b4b4b4;
    --card: #f5f3ee;
    --ink: #111111;
    --gold-light: #f1d77a;
    --gold: #d6b04a;
    --gold-deep: #b58f2e;
  }
  html, body {
    margin: 0;
    padding: 0;
    width: 1200px;
    height: 1200px;
    overflow: hidden;
    background: var(--backdrop);
  }
  .canvas {
    position: relative;
    width: 1200px;
    height: 1200px;
  }
  .card {
    position: absolute;
    left: 262px;
    width: 685px;
    height: 391px;
    background: var(--card);
    box-shadow: 0 14px 22px rgba(0,0,0,0.28);
  }
  .card--front { top: 165px; }
  .card--back  { top: 653px; }

  /* Front */
  .contact {
    position: absolute;
    left: 36px;
    top: 146px;
    font-family: "Montserrat", sans-serif;
    color: var(--ink);
  }
  .contact__name {
    margin: 0;
    font-family: "Oswald", sans-serif;
    font-weight: 500;
    font-size: 25px;
    letter-spacing: 0.5px;
    line-height: 1;
    color: var(--ink);
  }
  .contact__role {
    margin: 6px 0 0;
    font-weight: 700;
    font-size: 14px;
  }
  .contact__address {
    margin: 28px 0 0;
    font-weight: 500;
    font-size: 14.5px;
    line-height: 19px;
  }
  .contact__list {
    list-style: none;
    margin: 14px 0 0;
    padding: 0;
    font-weight: 500;
    font-size: 14.5px;
  }
  .contact__list li {
    display: flex;
    align-items: center;
    height: 19.5px;
  }
  .contact__list svg {
    width: 13px;
    height: 13px;
    margin-right: 10px;
    fill: var(--gold-deep);
    flex: none;
  }
  .front-mark {
    position: absolute;
    left: 330px;
    top: 40px;
    width: 320px;
    text-align: center;
  }
  .front-mark__dot {
    width: 170px;
    height: 170px;
    margin: 0 auto;
    border-radius: 50%;
    background: linear-gradient(135deg, var(--gold-light), var(--gold) 55%, var(--gold-deep));
  }
  .front-mark__name {
    margin: 22px 0 0;
    font-family: "Montserrat", sans-serif;
    font-weight: 700;
    font-size: 34px;
    letter-spacing: 1px;
    color: var(--ink);
  }

  /* Back */
  .back-mark {
    position: absolute;
    left: 0;
    right: 0;
    top: 94px;
    text-align: center;
    font-family: "Montserrat", sans-serif;
    font-weight: 700;
    color: var(--ink);
  }
  .back-mark__dot {
    width: 86px;
    height: 86px;
    margin: 0 auto 18px;
    border-radius: 50%;
    background: linear-gradient(135deg, var(--gold-light), var(--gold) 55%, var(--gold-deep));
  }
  .back-mark__name {
    margin: 0;
    font-size: 46px;
    line-height: 1;
    letter-spacing: 0.5px;
  }
  .back-mark__tag {
    margin: 6px 0 0;
    font-size: 20px;
    line-height: 1;
  }
</style>
</head>
<body>
<main class="canvas">

  <section class="card card--front" aria-label="Business card front">
    <div class="contact">
      <h1 class="contact__name">DANIEL HARPER</h1>
      <p class="contact__role">President</p>
      <p class="contact__address">4120 Willow Bend Road<br>Fairbanks, Alaska 34612</p>
      <ul class="contact__list">
        <li>
          <svg viewBox="0 0 16 16" aria-hidden="true"><path d="M3.2 1l2.6 3.2-1.5 1.8c.9 2 2.6 3.7 4.7 4.7l1.8-1.5L14 11.8 12.4 15C6.2 14.6 1.4 9.8 1 3.6z"/></svg>
          555-214-7731
        </li>
        <li>
          <svg viewBox="0 0 16 16" aria-hidden="true"><path d="M4.5 0h7A1.5 1.5 0 0 1 13 1.5v13A1.5 1.5 0 0 1 11.5 16h-7A1.5 1.5 0 0 1 3 14.5v-13A1.5 1.5 0 0 1 4.5 0zM5 2v10h6V2zm3 11a1 1 0 1 0 0 2 1 1 0 0 0 0-2z"/></svg>
          555-608-2149
        </li>
        <li>
          <svg viewBox="0 0 16 16" aria-hidden="true"><path d="M4 0h6l2 2v4H4zM1 7h14v6h-2v-2H3v2H1zm3 5h8v4H4z"/></svg>
          555-390-4476
        </li>
        <li>
          <svg viewBox="0 0 16 16" aria-hidden="true"><path d="M0 3h16v1.2L8 9 0 4.2zM0 5.6l8 4.8 8-4.8V13H0z"/></svg>
          info@maplecrestrealty.com
        </li>
        <li>
          <svg viewBox="0 0 16 16" aria-hidden="true"><path d="M8 0a8 8 0 1 0 0 16A8 8 0 0 0 8 0zm0 2c-.6 1-1 2.2-1.1 3.5H3a5 5 0 0 1 5-3.5zm-5 5h3.9c0 2 .5 3.8 1.1 5A5 5 0 0 1 3 7zm7 5.5c.6-1.2 1-3 1-5.5h2.6A5.9 5.9 0 0 1 10 12.5zM11 5.5C10.9 4.2 10.5 3 10 2.3a6 6 0 0 1 3.4 3.2z"/></svg>
          www.maplecrestrealty.com
        </li>
      </ul>
    </div>
    <div class="front-mark">
      <div class="front-mark__dot" aria-hidden="true"></div>
      <p class="front-mark__name">MAPLE CREST</p>
    </div>
  </section>

  <section class="card card--back" aria-label="Business card back">
    <div class="back-mark">
      <div class="back-mark__dot" aria-hidden="true"></div>
      <p class="back-mark__name">MAPLE CREST</p>
      <p class="back-mark__tag">REALESTATE</p>
    </div>
  </section>

</main>
</body>
</html>
```